CONTACT US Page and design for website

We need a contact us page for our website. We would like it to have a message area, a map, our information, etc.

Please see the text attachment for what we are looking for. We need to have something that is creative and interesting, modern and professional.

We believe that a contact US page should be very creative because everyone clicks that to contact us. We want it to be super professional, attention grabbing, pleasing to the eye.

PLEASE KEEP THE HEADER AND FOOTER THE SAME, ONLY THE ACTUAL CONTACT US PAGE NEEDS TO BE WORKED ON. THANKS!
We are excited to work with designers for this project.

Target Market(s)

Clients in technology business

Industry/Entity Type

Information Technology

Number of Pages Required

1 page

Font styles to use
Serif

Requirements
Must have
• CHECK THE TEXT ATTACHMENT PLEASE
• Must stay within our design colors and theme.
Nice to have
• see attachment
Should not have
• it should be special

```html
<!DOCTYPE html>
<html lang="en">
<head>
<meta charset="utf-8">
<title>Contact Us – Orbitek</title>
<link rel="stylesheet" href="https://fonts.googleapis.com/css2?family=Open+Sans:wght@300;400;600;700&family=Arimo:wght@400;700&display=swap">
<style>
:root{
  --teal:#3cc4b8;
  --teal-deep:#2b8b85;
  --teal-dark:#0c3a3b;
  --ink:#222;
  --muted:#555;
  --line:#d8d8d8;
  --tile:#f2f2f2;
  --footer:#a3a3a3;
  --footer-deep:#8f8f8f;
  --white:#fff;
}
*{box-sizing:border-box;margin:0;padding:0}
html,body{width:668px;height:1200px;overflow:hidden;background:var(--white)}
body{position:relative;font-family:"Open Sans",sans-serif;color:var(--ink)}
.abs{position:absolute}
/* header */
.brand{left:36px;top:12px;display:flex;align-items:center;gap:8px}
.brand-square{width:30px;height:30px;background:var(--teal)}
.brand-name{font-size:24px;font-weight:600;color:var(--teal);letter-spacing:2px}
.account-tab{left:530px;top:0;width:105px;height:18px;background:#b5b5b5;border-radius:0 0 10px 10px;display:flex;justify-content:space-around;align-items:center;font-size:7px;color:#333}
.quick{top:27px;display:flex;align-items:center;gap:6px;font-size:9px;color:#444}
.quick .dot{width:22px;height:22px;border-radius:50%;border:1px solid #cfe;background:#eefaf8;display:flex;align-items:center;justify-content:center}
.quick.phone span{font-size:12px;color:#222}
.nav{left:0;top:57px;width:668px;height:26px;border-top:1px solid var(--line);border-bottom:1px solid var(--line)}
.nav ul{list-style:none;display:flex;gap:14px;position:absolute;left:35px;top:8px;font-size:6.5px;color:#444}
.search{left:519px;top:63px;width:92px;height:17px;border:1px solid #bbb;border-radius:9px;font-size:7px;padding:4px 10px}
.search svg{position:absolute;right:6px;top:3px}
.cart{left:616px;top:61px;width:21px;height:21px;border-radius:50%;border:1px solid var(--teal);display:flex;align-items:center;justify-content:center}
.crumb{left:0;top:85px;width:668px;height:19px;background:linear-gradient(90deg,#2aa89e,var(--teal) 50%,#6fd8ce);font-size:7px;color:var(--white);padding:5px 73px;font-weight:600}
/* contact intro */
.page-title{left:65px;top:137px;font-size:28px;font-weight:300;letter-spacing:.5px}
.title-rule{left:65px;top:172px;width:163px;height:1px;background:var(--teal)}
.info{top:190px;font-size:9px;line-height:12px;color:#333}
.info h3{font-size:9.5px;font-weight:600;color:#222}
.divider{top:190px;height:38px;border-left:1px dotted #999}
.band-line{left:0;width:668px;height:2px;background:var(--teal)}
.map{left:0;top:249px;width:668px;height:224px;background:linear-gradient(135deg,#e8e8e6,#dedede 60%,#e4ecef)}
/* form section */
.hero{left:0;top:476px;width:668px;height:299px;background:radial-gradient(ellipse at 70% 30%,#24585a,var(--teal-dark) 55%,#061d1f)}
.form{left:67px;top:529px;width:335px;height:200px;background:var(--teal-deep)}
.field{left:10px;width:310px;border-bottom:1px solid rgba(255,255,255,.45);font-size:7.5px;color:var(--white);padding-bottom:3px}
.message-box{left:10px;top:101px;width:310px;height:59px;border:1px solid rgba(255,255,255,.45)}
.submit{left:10px;top:173px;width:57px;height:16px;background:#0f3133;color:var(--white);font-size:7px;display:flex;align-items:center;justify-content:center;gap:4px}
.hours{left:421px;top:540px;color:var(--white);width:160px}
.hours h2{font-size:13px;font-weight:400;padding-bottom:4px;border-bottom:1px solid var(--teal);width:159px}
.hours li{list-style:none;font-size:9.5px;margin-top:11.5px;display:flex;align-items:center;gap:4px}
.hours .clock{width:8px;height:8px;border:1px solid var(--white);border-radius:50%}
.hours p{font-size:7.5px;font-weight:700;margin-top:10px;padding-top:8px;border-top:1px solid rgba(255,255,255,.5);line-height:11px}
/* social */
.social{top:787px;width:127px;height:126px;background:var(--tile);display:flex;align-items:center;justify-content:center;font-size:15px;font-weight:700;color:#111}
/* footer */
.footer{left:0;top:929px;width:668px;height:175px;background:var(--footer);font-family:Arimo,sans-serif;color:var(--white)}
.about{left:204px;top:9px;width:292px;font-size:8px;line-height:11px;text-align:center}
.about-rule{left:180px;top:59px;width:330px;height:1px;background:rgba(255,255,255,.35)}
.contact-row{top:82px;font-size:8px;line-height:11px;display:flex;gap:5px}
.menu{top:116px;font-size:9px}
.support-links{left:436px;top:130px;font-size:5.5px;line-height:8px}
.footer-base{left:0;top:1104px;width:668px;height:96px;background:var(--footer-deep);font-family:Arimo,sans-serif;color:var(--white)}
.ring{top:10px;width:22px;height:22px;border-radius:50%;border:1px solid rgba(255,255,255,.7)}
.base-rule{left:100px;top:43px;width:468px;height:1px;background:rgba(255,255,255,.35)}
.base-brand{left:306px;top:54px;display:flex;gap:6px;font-size:7px;line-height:10px;align-items:flex-start}
.base-brand i{width:10px;height:10px;background:var(--white);display:block}
.chat-tab{left:541px;top:1187px;width:120px;height:13px;background:var(--teal);border:1px solid #2aa89e;border-radius:4px 4px 0 0;color:var(--white);font:700 7px/12px Georgia,serif;padding-left:6px}
</style>
</head>
<body>
<header>
  <div class="abs brand"><span class="brand-square"></span><span class="brand-name">ORBITEK</span></div>
  <div class="abs account-tab"><span>SIGN UP</span><span>LOGIN</span></div>
  <div class="abs quick" style="left:466px"><span class="dot"><svg width="10" height="10" viewBox="0 0 10 10"><path d="M1 2h8v5H4L2 9V7H1z" fill="#3cc4b8"/></svg></span>LIVE CHAT</div>
  <div class="abs quick phone" style="left:542px"><span class="dot"><svg width="10" height="10" viewBox="0 0 10 10"><path d="M2 1l2 2-1 1.5a6 6 0 0 0 2.5 2.5L7 6l2 2-1.5 1.5C4 9 1 6 .5 2.5z" fill="#3cc4b8"/></svg></span><span>555-240-7718</span></div>
  <nav class="abs nav"><ul><li>SERVERS</li><li>WORKSTATIONS</li><li>COMPONENTS</li><li>VIRTUAL REALITY</li><li>DRONES</li><li>ABOUT US</li><li>BLOG</li><li>RESOURCES</li><li>CONTACT US</li></ul></nav>
  <div class="abs search">Search<svg width="9" height="9" viewBox="0 0 9 9"><circle cx="3.8" cy="3.8" r="2.8" fill="none" stroke="#3cc4b8" stroke-width="1.3"/><path d="M6 6l2.4 2.4" stroke="#3cc4b8" stroke-width="1.3"/></svg></div>
  <div class="abs cart"><svg width="10" height="9" viewBox="0 0 10 9"><path d="M1 3h8l-1 5H2z" fill="none" stroke="#3cc4b8"/></svg></div>
  <div class="abs crumb">HOME / CONTACT US</div>
</header>

<main>
  <h1 class="abs page-title">CONTACT US</h1>
  <div class="abs title-rule"></div>
  <div class="abs info" style="left:67px">Orbitek Systems, LLC.<br>4820 Larkmoor Ave.<br>Westbrook, CA 90412</div>
  <div class="abs divider" style="left:193px"></div>
  <div class="abs info" style="left:224px"><h3>General Inquiries</h3>(555)240-7718<br>info@orbitekhq.com</div>
  <div class="abs divider" style="left:332px"></div>
  <div class="abs info" style="left:360px"><h3>Sales Inquiries</h3>(555)240-7718<br>sales@orbitekhq.com</div>
  <div class="abs divider" style="left:467px"></div>
  <div class="abs info" style="left:494px"><h3>Purchasing Inquiries</h3>(555)240-7719<br>purchasing@orbitekhq.com</div>

  <div class="abs band-line" style="top:247px"></div>
  <div class="abs map" role="img" aria-label="Street map showing the office location"></div>
  <div class="abs band-line" style="top:473px;height:3px"></div>

  <section class="abs hero" role="img" aria-label="Dark teal photo of a desk with keyboard and glasses"></section>
  <form class="abs form">
    <div class="abs field" style="top:14px">NAME</div>
    <div class="abs field" style="top:39px">EMAIL</div>
    <div class="abs field" style="top:63px">PHONE NUMBER</div>
    <div class="abs field" style="top:88px;border:0">MESSAGE</div>
    <div class="abs message-box"></div>
    <div class="abs submit"><svg width="7" height="5" viewBox="0 0 7 5"><rect x=".5" y=".5" width="6" height="4" fill="none" stroke="#fff"/><path d="M.5.5l3 2 3-2" fill="none" stroke="#fff"/></svg>SUBMIT</div>
  </form>
  <aside class="abs hours">
    <h2>HOURS OF OPERATION</h2>
    <ul>
      <li><span class="clock"></span>Monday: 8:00am- 5:00pm</li>
      <li><span class="clock"></span>Tuesday:8:00am- 5:00pm</li>
      <li><span class="clock"></span>Wednesday: 8:00am- 5:00pm</li>
      <li><span class="clock"></span>Thursday: 8:00am- 5:00pm</li>
      <li><span class="clock"></span>Friday: 8:00am- 5:00pm</li>
    </ul>
    <p>Our dedicated customer service representatives are available 24/7 by phone.</p>
  </aside>

  <div class="abs social" style="left:67px">Friendly</div>
  <div class="abs social" style="left:202px">Circlr</div>
  <div class="abs social" style="left:337px">Linkwise</div>
  <div class="abs social" style="left:472px">Snapframe</div>
</main>

<footer>
  <div class="abs footer">
    <p class="abs about">Based in Westbrook California, Orbitek offers custom servers, storage, and workstations for local businesses in Los Angeles, Beverly Hills, Thousand Oaks, Ventura, Orange County, Santa Barbara, Oxnard, Irvine, Anaheim, and San Diego. Orbitek also offers such products to clients throughout the United States and Worldwide.</p>
    <div class="abs about-rule"></div>
    <div class="abs contact-row" style="left:204px"><svg width="6" height="8" viewBox="0 0 6 8"><path d="M3 8L.5 3.5a2.5 2.5 0 1 1 5 0z" fill="#fff"/></svg><span>4820 Larkmoor Ave.<br>Westbrook, CA 90412</span></div>
    <div class="abs contact-row" style="left:305px"><svg width="7" height="7" viewBox="0 0 10 10"><path d="M2 1l2 2-1 1.5a6 6 0 0 0 2.5 2.5L7 6l2 2-1.5 1.5C4 9 1 6 .5 2.5z" fill="#fff"/></svg>555-240-7718</div>
    <div class="abs contact-row" style="left:395px"><svg width="8" height="6" viewBox="0 0 8 6"><rect width="8" height="6" fill="#fff"/></svg>sales@orbitekhq.com</div>
    <div class="abs menu" style="left:185px">Computer</div>
    <div class="abs menu" style="left:260px">Drones</div>
    <div class="abs menu" style="left:314px">Virtual</div>
    <div class="abs menu" style="left:377px">About</div>
    <div class="abs menu" style="left:426px">Customer Support</div>
    <div class="abs support-links">Terms and<br>Conditions<br>Warranty Information<br>Contact Us<br>Return Policy</div>
  </div>
  <div class="abs footer-base">
    <span class="abs ring" style="left:274px"></span>
    <span class="abs ring" style="left:304px"></span>
    <span class="abs ring" style="left:334px"></span>
    <span class="abs ring" style="left:364px"></span>
    <div class="abs base-rule"></div>
    <div class="abs base-brand"><i></i><span>Orbitek Systems, LLC.<br>Copyright © 2017</span></div>
  </div>
  <div class="abs chat-tab">CHAT NOW</div>
</footer>
</body>
</html>
```